Website Design for Freeze-Dried Food Manufacturing Company (Pet Food & Agri-Food)

We are looking for a high-level web designer to create a clean, modern, premium website design for Brindle, a freeze-dried food manufacturing company operating in both the pet food and agri-food space.
This is not a basic website build β we are looking for a designer who understands brand positioning, layout, and user flow, not just visuals.
π― Project Objective
Design a website that:
Clearly communicates our capabilities and value proposition
Feels premium, credible, and product-driven
Guides users through a simple, intuitive journey
Clean and Crips
A critical requirement is clearly separating:
π Pet Food
π Agri-Food
These must feel like two distinct pathways within the same brand experience.
We have attached detailed documents outlining structure, layout, and messaging. These should be followed closely.
π What Success Looks Like
A high-impact homepage with strong visual hierarchy
Clear entry points into Pet Food and Agri-Food
Clean, intentional layout (not cluttered or template-like)
Thoughtful spacing, typography, and flow
A design that feels considered and elevated, not generic
π¨ Design Direction
We are aiming for a:
Minimal, premium aesthetic
Warm, natural color palette (creams, browns, muted tones)
Ingredient and product-focused visuals
Avoid:
Overly corporate / industrial styles
Generic SaaS-style layouts
Busy or over-designed interfaces
End Goal
A website that immediately communicates:
Who we are
What we do
Why weβre different
In a way that feels premium, clear, and easy to navigate.
Link to current website: https://brindleharvest.example/
https://brindlelabs.example/wp-admin/

```html
<!DOCTYPE html>
<html lang="en">
<head>
<meta charset="utf-8">
<title>Brindle — Pet Food</title>
<link href="https://fonts.googleapis.com/css2?family=Playfair+Display:wght@400;500&family=Poppins:wght@300;400;500;600&display=swap" rel="stylesheet">
<style>
:root{
  --cream:#f7f2ea;
  --cream-deep:#efe4d6;
  --brown:#b8764a;
  --brown-dark:#9c5f37;
  --ink:#3a2a20;
  --text:#5a4a40;
  --line:#c99a78;
  --white:#ffffff;
}
*{margin:0;padding:0;box-sizing:border-box}
html,body{width:1200px;height:3392px;overflow:hidden}
body{background:var(--cream);font-family:'Poppins',sans-serif;color:var(--ink);position:relative}
.abs{position:absolute}
.serif{font-family:'Playfair Display',serif}
.wordmark{font-family:'Poppins',sans-serif;font-weight:300;color:var(--brown);font-size:44px;letter-spacing:1px;line-height:1}

/* header */
.site-header{position:absolute;left:0;top:0;width:1200px;height:110px;z-index:5}
.site-nav{position:absolute;top:56px;left:356px;display:flex;gap:24px;font-size:12.5px;font-weight:500}
.site-nav a{color:var(--ink);text-decoration:none}
.site-nav a.active{color:var(--brown);border-bottom:1px solid var(--brown);padding-bottom:2px}
.btn{display:inline-flex;align-items:center;justify-content:center;border-radius:30px;font-weight:600;text-transform:uppercase;text-decoration:none;font-size:15px;color:var(--white);background:linear-gradient(90deg,#c7834f,#a8673d);box-shadow:0 4px 10px rgba(150,90,50,.25)}

/* hero */
.hero-photo{left:700px;top:0;width:500px;height:592px;z-index:1;clip-path:polygon(392px 0,500px 0,500px 592px,168px 592px,5px 375px);background:linear-gradient(135deg,#e8d4bc 0%,#c89a6c 40%,#8f6a4c 70%,#d9c6b1 100%)}
.hero-rule{left:112px;top:186px;width:3px;height:376px;background:var(--ink)}
.eyebrow{left:145px;top:219px;color:var(--brown);font-size:17px;font-weight:500}
.eyebrow-line{left:303px;top:230px;width:308px;height:1px;background:var(--line)}
.hero-title{left:145px;top:246px;font-size:51px;line-height:56px;font-weight:400;color:var(--ink)}
.hero-copy{left:148px;top:366px;width:470px;font-size:18px;line-height:31px;font-weight:500;color:var(--text)}

/* section titles */
.section-title{width:1200px;left:0;text-align:center;font-family:'Playfair Display',serif;font-size:46px;font-weight:400;text-transform:uppercase;color:var(--ink);line-height:57px}
.title-rule{left:556px;width:88px;height:2px;background:var(--brown)}

/* applications */
.app-card{top:785px;width:304px;text-align:center}
.app-img{width:304px;height:212px;border-radius:6px;box-shadow:0 8px 18px rgba(90,60,40,.18)}
.app-card h3{margin-top:23px;font-size:18px;font-weight:500;line-height:28px;text-transform:uppercase;color:var(--ink)}
.dot{width:7px;height:7px;border-radius:50%;background:var(--brown);margin:10px auto 13px}
.app-card p{font-size:17px;line-height:28px;color:var(--text)}

/* fulfilment */
.fulfil-band{left:0;top:1230px;width:1200px;height:785px;background:linear-gradient(180deg,var(--cream) 0%,#f1e9df 45%,#eadfd2 100%)}
.lede{width:1200px;left:0;text-align:center;font-size:18px;color:var(--ink)}
.step{width:300px;text-align:center}
.step h4{font-size:17px;font-weight:500;text-transform:uppercase;color:var(--ink);line-height:26px}
.step p{font-size:17px;line-height:28px;color:var(--text)}
.step-ring{width:124px;height:124px;border-radius:50%;border:4px solid var(--brown);background:var(--cream);box-shadow:0 8px 16px rgba(120,80,50,.2);display:flex;align-items:center;justify-content:center}

/* why */
.why-label h4{font-size:18px;font-weight:500;text-transform:uppercase;color:var(--ink);line-height:30px}
.why-label p{font-size:17px;line-height:28px;color:var(--text)}
.why-left{text-align:right;width:300px}
.why-right{text-align:left;width:230px}

/* brand band */
.support-band{left:0;top:2753px;width:1200px;height:428px;background:linear-gradient(180deg,#c08159 0%,#b77853 55%,#a66c49 100%)}
.support-title{width:1200px;left:0;top:2850px;text-align:center;color:var(--white);font-family:'Playfair Display',serif;font-size:46px;font-weight:400;text-transform:uppercase}
.support-copy{left:150px;width:900px;top:2938px;text-align:center;color:var(--white);font-size:19px;line-height:30px}
.btn-light{background:var(--white);color:var(--ink);box-shadow:none}

/* footer */
.foot-nav{position:absolute;top:3261px;right:112px;display:flex;gap:26px;font-size:13px;font-weight:500}
.foot-nav a{color:var(--ink);text-decoration:none}
.foot-rule{left:112px;top:3312px;width:976px;height:1px;background:#ddd0c2}
.copyright{width:1200px;left:0;top:3340px;text-align:center;font-size:11px;color:var(--text)}
.social{width:36px;height:36px;border-radius:50%;background:var(--white);top:3329px;box-shadow:0 2px 6px rgba(0,0,0,.06)}
.social.filled{background:var(--brown)}
</style>
</head>
<body>

<!-- Hero image -->
<div class="abs hero-photo" role="img" aria-label="Golden retriever and tabby cat beside a bowl of freeze-dried food in a bright kitchen"></div>

<!-- Header -->
<header class="site-header">
  <div class="abs wordmark" style="left:111px;top:40px">Brindle</div>
  <nav class="site-nav">
    <a href="#">Home</a><a href="#">About</a><a href="#">Agri-Food</a><a href="#" class="active">Pet Food</a><a href="#">Facilities</a><a href="#">Sustainability</a><a href="#">Our Process</a>
  </nav>
  <a class="abs btn" href="#" style="left:957px;top:41px;width:131px;height:47px">Contact</a>
</header>

<!-- Hero -->
<div class="abs hero-rule"></div>
<div class="abs eyebrow">PET FOOD</div>
<div class="abs eyebrow-line"></div>
<h1 class="abs hero-title serif">Freeze Dried. Real<br>Nutrition. Pets Thrive.</h1>
<p class="abs hero-copy">High quality freeze dried ingredients and co-manufacturing solutions for complete and supplemental pet food.</p>
<a class="abs btn" href="#" style="left:147px;top:477px;width:189px;height:47px;font-size:14px">Request a Quote</a>

<!-- Applications -->
<h2 class="abs section-title" style="top:676px">Our Applications</h2>
<div class="abs title-rule" style="top:740px"></div>

<div class="abs app-card" style="left:112px">
  <div class="app-img" role="img" aria-label="Scoop of freeze-dried kibble with a small dog in the background" style="background:linear-gradient(135deg,#5d4232,#a47552 50%,#6b4a33)"></div>
  <h3>Complete and Balanced<br>Meals</h3>
  <div class="dot"></div>
  <p>Freeze dried solutions for<br>complete and supplemental<br>diets tailored to your brand.</p>
</div>
<div class="abs app-card" style="left:448px">
  <div class="app-img" role="img" aria-label="Pet food packages and bowls of toppers on a wooden table" style="background:linear-gradient(135deg,#a06a43,#d9c3a6 50%,#8f5d3a)"></div>
  <h3>Meal Enhancement<br>Toppers</h3>
  <div class="dot"></div>
  <p>Nutrient-rich toppers to enhance<br>palatability and boost the<br>nutrition in any bowl.</p>
</div>
<div class="abs app-card" style="left:782px">
  <div class="app-img" role="img" aria-label="Woman pouring treats from a paper bag into a storage container in a pantry" style="background:linear-gradient(135deg,#cfc5b8,#8a7664 50%,#e6ddd2)"></div>
  <h3>Single Ingredient<br>Treats</h3>
  <div class="dot"></div>
  <p>Pure, high-protein treats made<br>from one ingredient. Simple.<br>Clean. Loved by pets.</p>
</div>

<!-- Fulfilment -->
<div class="abs fulfil-band"></div>
<h2 class="abs section-title" style="top:1262px">Pick, Pack &amp; Ship —<br>We Handle the Details</h2>
<div class="abs title-rule" style="top:1382px"></div>
<p class="abs lede" style="top:1412px">Let us take care of fulfillment so you can focus on growing your brand.</p>

<svg class="abs" style="left:0;top:1590px" width="1200" height="240" viewBox="0 0 1200 240">
  <line x1="249" y1="126" x2="950" y2="126" stroke="#b8764a" stroke-width="2"/>
  <line x1="249" y1="20" x2="249" y2="64" stroke="#7a5a44" stroke-width="2"/>
  <circle cx="249" cy="20" r="5" fill="#9c5f37"/>
  <line x1="715" y1="20" x2="715" y2="64" stroke="#7a5a44" stroke-width="2"/>
  <circle cx="715" cy="20" r="5" fill="#9c5f37"/>
  <line x1="482" y1="188" x2="482" y2="230" stroke="#b8764a" stroke-width="2"/>
  <circle cx="482" cy="230" r="5" fill="#b8764a"/>
  <line x1="950" y1="188" x2="950" y2="230" stroke="#b8764a" stroke-width="2"/>
  <circle cx="950" cy="230" r="5" fill="#b8764a"/>
</svg>

<div class="abs step-ring" style="left:187px;top:1654px">
  <svg width="60" height="60" viewBox="0 0 60 60" fill="none" stroke="#b8764a" stroke-width="2" stroke-linejoin="round"><path d="M10 22 L30 14 L50 22 L30 30 Z"/><path d="M10 22 V44 L30 52 V30"/><path d="M50 22 V44 L30 52"/><path d="M23 11 l4 4 l8 -8"/></svg>
</div>
<div class="abs step-ring" style="left:420px;top:1654px">
  <svg width="64" height="60" viewBox="0 0 64 60" fill="none" stroke="#b8764a" stroke-width="2" stroke-linejoin="round"><path d="M6 10 H14 V44 H56"/><rect x="20" y="30" width="12" height="12"/><rect x="34" y="30" width="12" height="12"/><rect x="27" y="18" width="12" height="12"/><circle cx="20" cy="50" r="4"/><circle cx="50" cy="50" r="4"/><path d="M42 10 l4 4 l8 -8"/></svg>
</div>
<div class="abs step-ring" style="left:653px;top:1654px">
  <svg width="64" height="60" viewBox="0 0 64 60" fill="none" stroke="#b8764a" stroke-width="2" stroke-linejoin="round"><rect x="8" y="28" width="26" height="18"/><path d="M34 34 H44 L50 40 V46 H34"/><circle cx="16" cy="48" r="4"/><circle cx="42" cy="48" r="4"/><path d="M30 22 c0 -8 12 -8 12 0 c0 6 -6 10 -6 10 s-6 -4 -6 -10z"/><circle cx="36" cy="21" r="2"/></svg>
</div>
<div class="abs step-ring" style="left:888px;top:1654px">
  <svg width="60" height="60" viewBox="0 0 60 60" fill="none" stroke="#b8764a" stroke-width="2" stroke-linejoin="round"><rect x="12" y="10" width="28" height="40" rx="2"/><rect x="20" y="6" width="12" height="6"/><path d="M18 22 H34 M18 28 H30 M18 34 H26"/><circle cx="38" cy="38" r="8"/><path d="M34 38 l3 3 l5 -5 M44 44 L52 52"/></svg>
</div>

<div class="abs step" style="left:99px;top:1475px"><h4>Pick</h4><p>Accurate picking and quality<br>checks to ensure every order is<br>perfect.</p></div>
<div class="abs step" style="left:565px;top:1475px"><h4>Ship</h4><p>Global shipping solutions with<br>reliable carriers and on-time<br>delivery.</p></div>
<div class="abs step" style="left:332px;top:1835px"><h4>Pack</h4><p>Secure, branded packaging<br>options tailored to your product<br>and customer.</p></div>
<div class="abs step" style="left:800px;top:1835px"><h4>Track</h4><p>Real-time tracking and<br>updates for complete visibility<br>and peace of mind.</p></div>

<!-- Why -->
<h2 class="abs section-title" style="top:2124px">Why Brindle</h2>
<div class="abs title-rule" style="top:2188px"></div>

<div class="abs" style="left:470px;top:2293px;width:260px;height:260px;transform:rotate(45deg);border-radius:42px;background:var(--cream);box-shadow:0 10px 30px rgba(120,90,60,.12)"></div>
<div class="abs wordmark" style="left:0;width:1200px;text-align:center;top:2394px;font-size:58px">Brindle</div>

<svg class="abs" style="left:0;top:2240px" width="1200" height="380" viewBox="0 0 1200 380" fill="none" stroke="#b8764a" stroke-width="1.6" stroke-linejoin="round">
  <rect x="351" y="34" width="64" height="64" rx="10" transform="rotate(45 383 66) translate(-8 -8)" fill="#f7f2ea"/>
  <rect x="351" y="34" width="64" height="64" rx="10" transform="rotate(45 820 66) translate(429 -8)" fill="#f7f2ea"/>
  <rect x="351" y="34" width="64" height="64" rx="10" transform="rotate(45 383 321) translate(-8 247)" fill="#f7f2ea"/>
  <rect x="351" y="34" width="64" height="64" rx="10" transform="rotate(45 820 321) translate(429 247)" fill="#f7f2ea"/>
  <path d="M375 46 L386 42 L397 46 V56 C397 64 386 70 386 70 C386 70 375 64 375 56 Z"/><path d="M381 56 l4 4 l7 -7"/><path d="M364 62 v10 l10 8 M408 62 v10 l-10 8"/>
  <circle cx="821" cy="58" r="8"/><circle cx="821" cy="58" r="15" stroke-dasharray="5 4"/><path d="M802 58 a19 19 0 0 1 33 -13 M840 58 a19 19 0 0 1 -33 13"/>
  <path d="M374 302 h10 a4 4 0 0 1 8 0 h10 v10 a4 4 0 0 1 0 8 v10 h-28 z"/><path d="M372 296 l-5 -5 M404 296 l5 -5 M388 290 v-6"/>
  <path d="M804 332 h34"/><rect x="808" y="316" width="5" height="16"/><rect x="816" y="310" width="5" height="22"/><rect x="824" y="304" width="5" height="28"/><rect x="832" y="298" width="5" height="34"/><circle cx="812" cy="296" r="6"/><path d="M830 294 l6 -6 M832 288 h4 v4"/>
</svg>

<div class="abs why-label why-left" style="left:7px;top:2236px"><h4>Quality You<br>Can Trust</h4><p>Rigorous standards.<br>Consistent results.</p></div>
<div class="abs why-label why-right" style="left:892px;top:2251px"><h4>Scalable Capacity</h4><p>Room to grow with your<br>business.</p></div>
<div class="abs why-label why-left" style="left:7px;top:2504px"><h4>Flexible Solutions</h4><p>Tailored to your product<br>and production needs.</p></div>
<div class="abs why-label why-right" style="left:892px;top:2493px"><h4>Built for Growth</h4><p>Partnerships that<br>support your long-term<br>goals.</p></div>

<!-- Support band -->
<div class="abs support-band" role="img" aria-label="Faded view of a production facility with piles of freeze-dried ingredients, under a warm brown tint"></div>
<h2 class="abs support-title">Your Brand, Our Support</h2>
<p class="abs support-copy">From order fulfillment to logistics, we act as an extension of your team—providing a seamless experience for you and your customers.</p>
<a class="abs btn btn-light" href="#" style="left:522px;top:3025px;width:154px;height:46px;font-size:14px">Learn More</a>

<!-- Footer -->
<div class="abs wordmark" style="left:111px;top:3250px">Brindle</div>
<nav class="foot-nav">
  <a href="#">Home</a><a href="#">About</a><a href="#">Agri-Food</a><a href="#">Pet Food</a><a href="#">Facilities</a><a href="#">Sustainability</a><a href="#">Our Process</a><a href="#">Contact</a>
</nav>
<div class="abs foot-rule"></div>
<p class="abs copyright">© 2026 ALL RIGHTS RESERVED</p>
<div class="abs social filled" style="left:965px" aria-label="Social link 1"></div>
<div class="abs social" style="left:1007px" aria-label="Social link 2"></div>
<div class="abs social" style="left:1050px" aria-label="Social link 3"></div>

</body>
</html>
```